Brivelo Website Design - Wordpress

Need a website WordPress design for our existing website that we just stood up. The logo is already in place and name. Brivelo.example We are a company which makes connections with our clients through educating them and providing networking events. We would like for the website to show a VIP/special feel to it.

Target Market(s)

Business executives and employees. Age group 26-65 in the following sectors:
- Technology
- Human Resources
- Finance
- Sales

Industry/Entity Type

Technical Service

Number of Pages Required

4 page

Font styles to use
Sans Serif

Requirements
Must have
• Must be something for Wordpress
Nice to have
• Would like this to be professional but look cutting edge and VIP.

```html
<!DOCTYPE html>
<html lang="en">
<head>
<meta charset="utf-8">
<title>Brivelo — Connected</title>
<link href="https://fonts.googleapis.com/css2?family=Montserrat:wght@400;500;600;700;800&family=Open+Sans:wght@400;600&display=swap" rel="stylesheet">
<style>
:root{
  --black:#000;
  --white:#fff;
  --ink:#1a1a1a;
  --muted:#555;
  --blue:#1c6fa0;
  --blue-deep:#0f4f7d;
  --red:#d22a25;
  --purple:#6e3a8c;
  --gold:#e2aa14;
  --teal:#136a8c;
  --green:#2f8a3d;
}
*{margin:0;padding:0;box-sizing:border-box}
html,body{width:1200px;height:4063px;overflow:hidden;background:var(--white)}
body{position:relative;font-family:"Open Sans",sans-serif;color:var(--ink)}
.abs{position:absolute}
h1,h2,h3,h4,.head{font-family:"Montserrat",sans-serif}

/* header */
.site-header{left:0;top:0;width:1200px;height:122px;background:var(--black)}
.brand{display:flex;align-items:center;gap:16px;color:var(--white);font-family:"Montserrat",sans-serif;font-weight:500;font-size:40px;letter-spacing:6px}
.brand-mark{width:34px;height:34px;background:var(--purple)}
.site-header .brand{left:116px;top:38px}
.header-phone{right:112px;top:18px;display:flex;align-items:center;gap:10px;color:var(--white);font-family:"Montserrat",sans-serif;font-weight:600;font-size:15px}
.header-phone .ring{width:34px;height:34px;border-radius:50%;background:var(--purple);display:flex;align-items:center;justify-content:center}
.main-nav{right:112px;top:76px;display:flex;gap:36px;color:var(--white);font-family:"Montserrat",sans-serif;font-weight:500;font-size:15px;letter-spacing:.5px}

/* hero */
.hero-image{left:0;top:122px;width:1200px;height:628px;background:linear-gradient(100deg,#12263d 0%,#234a6b 35%,#8a3a22 65%,#c9561e 85%,#5a2a1a 100%)}
.hero-bands{left:0;top:560px}
.hero-title{left:111px;top:300px;color:var(--white);font-size:50px;font-weight:800;letter-spacing:.5px}
.hero-text{left:111px;top:368px;width:600px;color:var(--white);font-size:18px;font-weight:600;line-height:29px}
.btn{display:flex;align-items:center;justify-content:center;background:var(--purple);color:var(--white);font-family:"Montserrat",sans-serif;font-weight:700;font-size:16px}
.hero-btn{left:111px;top:450px;width:154px;height:48px}
.slider-dots{left:1134px;top:362px}

/* strategy */
.section-title{width:1200px;left:0;text-align:center;font-weight:700;font-size:34px;letter-spacing:1px;color:var(--black)}
.section-sub{left:300px;width:600px;text-align:center;font-size:16px;line-height:29px;color:#333}
.pillar{font-family:"Montserrat",sans-serif}
.pillar b{display:block;font-weight:500;font-size:30px;line-height:34px}
.pillar span{display:block;font-size:16px;color:#333}
.strategy-mark{left:441px;top:1070px;width:317px;height:398px;background:linear-gradient(135deg,#1c6fa0 0%,#6e3a8c 40%,#d22a25 60%,#e2aa14 100%);opacity:.9}

/* offer */
.offer-bg{left:0;top:1585px}
.offer-kicker{left:111px;top:1733px;color:var(--white);font-family:"Montserrat",sans-serif;font-weight:500;font-size:24px}
.offer-title{left:111px;top:1775px;color:var(--white);font-weight:600;font-size:31px;letter-spacing:.5px}
.offer-text{left:111px;top:1828px;width:422px;color:var(--white);font-size:14.5px;line-height:29.5px;text-align:justify}
.offer-btn{left:111px;top:2208px;width:154px;height:46px}
.tile{width:238px;height:236px;padding:26px 34px;color:var(--white)}
.tile h3{font-size:21px;font-weight:600;margin:20px 0 6px}
.tile p{font-size:14px;line-height:24px}
.tile.educate{left:585px;top:1736px;background:var(--teal)}
.tile.equip{left:848px;top:1736px;background:var(--red)}
.tile.exchange{left:585px;top:2002px;background:var(--purple)}
.tile.expand{left:848px;top:2002px;background:var(--gold)}

/* about */
.portrait{width:214px;height:214px;border-radius:50%;border:6px solid var(--purple);background:radial-gradient(circle at 50% 40%,#b9a79a 0%,#8a7a72 45%,#e8e8e8 75%)}
.member h4{font-size:21px;font-weight:700;letter-spacing:1px;color:var(--black);margin-bottom:12px}
.member p{font-size:15.5px;line-height:26px;color:#555}

/* quote */
.quote-map{left:600px;top:3007px;width:600px;height:663px;background:linear-gradient(160deg,#e9e4d6 0%,#ddd8c6 50%,#cfd6c4 100%)}
.quote-panel{left:0;top:3007px}
.quote-title{left:150px;top:3085px;color:var(--white);font-weight:700;font-size:35px;letter-spacing:1px}
.field{left:150px;width:445px;border-bottom:2px solid rgba(255,255,255,.85);color:var(--white);font-size:15px;padding:0 0 10px 0;display:flex;align-items:center;gap:12px}
.submit{left:152px;top:3497px;width:233px;height:66px;border:3px solid var(--white);color:var(--white);display:flex;align-items:center;justify-content:center;font-family:"Montserrat",sans-serif;font-weight:600;font-size:24px;letter-spacing:2px}
.map-pin{left:904px;top:3208px}

/* footer */
.site-footer{left:0;top:3670px;width:1200px;height:393px;background:var(--black);color:var(--white)}
.footer-heading{font-weight:600;font-size:21px;letter-spacing:1px}
.footer-links{list-style:none;font-size:15.5px;line-height:32.5px}
.contact-line{display:flex;gap:16px;font-size:15.5px;line-height:24px}
.copyright{left:116px;top:3993px;font-size:15px;color:var(--white)}
.social{left:962px;top:3985px;display:flex;gap:10px}
.social i{width:35px;height:35px;border:2px solid var(--white);border-radius:50%;display:block}
</style>
</head>
<body>

<header class="site-header abs">
  <div class="brand abs"><span class="brand-mark"></span>BRIVELO</div>
  <div class="header-phone abs">
    <span class="ring"><svg width="18" height="18" viewBox="0 0 24 24"><path fill="#fff" d="M6.6 10.8a15 15 0 006.6 6.6l2.2-2.2c.3-.3.7-.4 1-.2 1.1.4 2.3.6 3.6.6.6 0 1 .4 1 1V20c0 .6-.4 1-1 1A17 17 0 013 4c0-.6.4-1 1-1h3.5c.6 0 1 .4 1 1 0 1.3.2 2.5.6 3.6.1.3 0 .7-.2 1z"/></svg></span>
    1-855-555-0142
  </div>
  <nav class="main-nav abs"><span>EVENTS</span><span>EXPAND</span><span>X</span><span>ABOUT</span><span>CONNECT</span></nav>
</header>

<section class="hero">
  <div class="hero-image abs" role="img" aria-label="Close-up photograph of glowing fibre-optic cables over a digital blue background"></div>
  <svg class="hero-bands abs" width="1200" height="200" viewBox="0 0 1200 200">
    <polygon points="0,70 600,120 1200,40 1200,190 0,190" fill="#fff"/>
    <polygon points="0,70 600,110 420,190 0,150" fill="#1c6fa0"/>
    <polygon points="0,70 420,90 200,180 0,160" fill="#0f4f7d" opacity=".7"/>
    <polygon points="600,110 1200,40 1200,115 760,170" fill="#d22a25"/>
    <polygon points="420,190 600,110 760,170 1200,115 1200,120 600,190" fill="#fff"/>
  </svg>
  <h1 class="hero-title abs">EXPAND YOUR BUSINESS</h1>
  <p class="hero-text abs">Our team is an unusual mix. We're globally experienced, technically capable, community focussed and highly fruitful.</p>
  <a class="btn hero-btn abs">Read More</a>
  <svg class="slider-dots abs" width="26" height="90" viewBox="0 0 26 90">
    <circle cx="13" cy="13" r="11" fill="none" stroke="#fff" stroke-width="2"/><circle cx="13" cy="13" r="6" fill="#fff"/>
    <circle cx="13" cy="50" r="6" fill="#fff"/><circle cx="13" cy="77" r="6" fill="#fff"/>
  </svg>
</section>

<section class="strategy">
  <h2 class="section-title abs" style="top:845px">IT'S ABOUT OUR UNIQUE X STRATEGY</h2>
  <p class="section-sub abs" style="top:910px">BRIVELO provides impactful connection opportunities to help educate, equip and expand you and your business</p>
  <div class="pillar abs" style="left:144px;top:1020px"><b style="color:var(--blue)">Mind</b><span>Thought</span></div>
  <div class="pillar abs" style="left:924px;top:1020px"><b style="color:var(--red)">Heart</b><span>Emotions</span></div>
  <div class="pillar abs" style="left:149px;top:1405px"><b style="color:var(--purple)">Soul</b><span>Intuition</span></div>
  <div class="pillar abs" style="left:931px;top:1405px"><b style="color:var(--gold)">Strength</b><span>Energy</span></div>
  <svg class="abs" style="left:0;top:1000px" width="1200" height="460" viewBox="0 0 1200 460">
    <g fill="none" stroke="#888" stroke-width="2" stroke-dasharray="6 5">
      <polyline points="480,88 480,38 258,38"/><polyline points="700,88 700,38 920,38"/>
      <polyline points="480,400 480,427 258,427"/><polyline points="700,400 700,427 920,427"/>
    </g>
    <g fill="#888"><polygon points="252,38 262,32 262,44"/><polygon points="926,38 916,32 916,44"/><polygon points="252,427 262,421 262,433"/><polygon points="926,427 916,421 916,433"/></g>
  </svg>
  <div class="strategy-mark abs" role="img" aria-label="Large four-colour brand symbol representing mind, heart, soul and strength"></div>
</section>

<section class="offer">
  <svg class="offer-bg abs" width="1200" height="800" viewBox="0 0 1200 800">
    <defs><linearGradient id="offerFill" x1="0" y1="0" x2="1" y2="1"><stop offset="0" stop-color="#1d6a9c"/><stop offset="1" stop-color="#185b8a"/></linearGradient></defs>
    <polygon points="0,30 600,0 1200,50 1200,730 600,800 0,740" fill="url(#offerFill)"/>
  </svg>
  <p class="offer-kicker abs">What we offer you</p>
  <h2 class="offer-title abs">OUR UNIQUE X STRATEGY</h2>
  <p class="offer-text abs">BRIVELO is powerfully effective because our approach is humanalistic. Our materials are founded upon the idea that Culture is a Person. Marcus Hale developed his philosophy on culture over more than three decades, learning from leaders and communities around the globe. We understand at the deepest level that culture is the heartbeat of your company, and as a healthy, strong heart means a healthy, strong person, culture works in a similar fashion. We use the letter X to illustrate this. Similar to how a person is made up of essentially four parts, our programs develop the four pieces of you and your company: thought, emotions, intuition and strength.</p>
  <a class="btn offer-btn abs">Read More</a>

  <div class="tile educate abs">
    <svg width="62" height="66" viewBox="0 0 62 66" fill="none" stroke="#fff" stroke-width="2.5"><path d="M31 14a15 15 0 00-9 27v7h18v-7a15 15 0 00-9-27z"/><path d="M24 54h14M26 60h10"/><path d="M31 2v6M8 12l5 4M54 12l-5 4M2 30h6M54 30h6"/></svg>
    <h3>EDUCATE</h3><p>At Brivelo, We Provide Effective Training And Learning</p>
  </div>
  <div class="tile equip abs">
    <svg width="62" height="66" viewBox="0 0 62 66" fill="none" stroke="#fff" stroke-width="2.5"><circle cx="31" cy="26" r="18" stroke-dasharray="5 3"/><circle cx="31" cy="22" r="6"/><path d="M20 38c2-6 6-8 11-8s9 2 11 8"/><path d="M22 50l-4 12M40 50l4 12"/></svg>
    <h3>EQUIP</h3><p>Through Our Connected Ecosystem Of Companies</p>
  </div>
  <div class="tile exchange abs">
    <svg width="66" height="60" viewBox="0 0 66 60" fill="none" stroke="#fff" stroke-width="3"><path d="M6 20h48M42 8l12 12-12 12"/><path d="M60 42H12M24 30L12 42l12 12"/></svg>
    <h3>EXCHANGE</h3><p>We Connect You With Others Who Have Successfully</p>
  </div>
  <div class="tile expand abs">
    <svg width="66" height="62" viewBox="0 0 66 62" fill="none" stroke="#fff" stroke-width="3"><path d="M6 6l18 18M6 6h12M6 6v12"/><path d="M60 6L42 24M60 6H48M60 6v12"/><path d="M6 56l18-18M6 56h12M6 56V44"/><path d="M60 56L42 38M60 56H48M60 56V44"/></svg>
    <h3>EXPAND</h3><p>Our goal is to help you and your business increase</p>
  </div>
</section>

<section class="about">
  <h2 class="section-title abs" style="top:2505px">ABOUT US</h2>
  <p class="section-sub abs" style="top:2570px;left:260px;width:680px;font-size:14.5px;line-height:26px">Our team is an unusual mix. We're globally experienced, technically capable, community focussed and highly fruitful. The four core values above inform everything we do. Our special sauce is knowing how to fuse structure and productivity with relationship and creativity.</p>
  <div class="portrait abs" style="left:127px;top:2691px" role="img" aria-label="Portrait photo of Marcus Hale"></div>
  <div class="member abs" style="left:366px;top:2734px;width:220px"><h4>MARCUS HALE</h4><p>Director of Communications; fusing culture, branding and marketing to facilitate clear, effective messaging.</p></div>
  <div class="portrait abs" style="left:605px;top:2691px" role="img" aria-label="Portrait photo of Daniel Reyes"></div>
  <div class="member abs" style="left:848px;top:2734px;width:260px"><h4>DANIEL REYES</h4><p>Greater Denver AreaInformation Technology and Services</p></div>
</section>

<section class="quote">
  <div class="quote-map abs" role="img" aria-label="Road map of the Missouri and Illinois region with a location pin"></div>
  <svg class="quote-panel abs" width="640" height="663" viewBox="0 0 640 663"><polygon points="0,0 628,0 600,663 0,663" fill="#6e3a8c"/></svg>
  <svg class="map-pin abs" width="52" height="64" viewBox="0 0 52 64"><path d="M26 2a24 24 0 00-24 24c0 18 24 36 24 36s24-18 24-36A24 24 0 0026 2z" fill="#6e3a8c"/><path d="M15 28l11-10 11 10v10H15z" fill="#fff"/></svg>
  <h2 class="quote-title abs">GET A QUOTE</h2>
  <div class="field abs" style="top:3165px"><svg width="13" height="14" viewBox="0 0 13 14" fill="#fff"><circle cx="6.5" cy="4" r="3.5"/><path d="M0 14c0-4 3-6 6.5-6s6.5 2 6.5 6z"/></svg>Name</div>
  <div class="field abs" style="top:3240px"><svg width="15" height="11" viewBox="0 0 15 11" fill="none" stroke="#fff" stroke-width="1.5"><rect x="1" y="1" width="13" height="9"/><path d="M1 1l6.5 5L14 1"/></svg>Email</div>
  <div class="field abs" style="top:3316px"><svg width="14" height="14" viewBox="0 0 24 24" fill="#fff"><path d="M6.6 10.8a15 15 0 006.6 6.6l2.2-2.2c.3-.3.7-.4 1-.2 1.1.4 2.3.6 3.6.6.6 0 1 .4 1 1V20c0 .6-.4 1-1 1A17 17 0 013 4c0-.6.4-1 1-1h3.5c.6 0 1 .4 1 1 0 1.3.2 2.5.6 3.6.1.3 0 .7-.2 1z"/></svg>Phone Number</div>
  <div class="field abs" style="top:3370px;height:88px;align-items:flex-start"><svg width="14" height="12" viewBox="0 0 14 12" fill="#fff"><path d="M0 0h14v9H4l-4 3z"/></svg>Message...</div>
  <div class="submit abs">SUBMIT</div>
</section>

<footer class="site-footer abs">
  <div class="brand abs" style="left:116px;top:100px"><span class="brand-mark"></span>BRIVELO</div>
  <h4 class="footer-heading abs" style="left:577px;top:40px">QUICK LINKS</h4>
  <ul class="footer-links abs" style="left:580px;top:86px"><li>Events</li><li>Expand</li><li>X</li><li>About</li><li>Connect</li></ul>
  <h4 class="footer-heading abs" style="left:843px;top:40px">CONTACT US</h4>
  <div class="contact-line abs" style="left:845px;top:84px">
    <svg width="16" height="22" viewBox="0 0 16 22" fill="#fff"><path d="M8 0a8 8 0 00-8 8c0 6 8 14 8 14s8-8 8-14a8 8 0 00-8-8zm0 11a3 3 0 110-6 3 3 0 010 6z"/></svg>
    <div>BRIVELO<br>120 Harbor Lane<br>Fairview, NJ 07000<br>Service License # 204</div>
  </div>
  <div class="contact-line abs" style="left:845px;top:208px">
    <svg width="18" height="18" viewBox="0 0 24 24" fill="none" stroke="#fff" stroke-width="2"><path d="M6.6 10.8a15 15 0 006.6 6.6l2.2-2.2c.3-.3.7-.4 1-.2 1.1.4 2.3.6 3.6.6.6 0 1 .4 1 1V20c0 .6-.4 1-1 1A17 17 0 013 4c0-.6.4-1 1-1h3.5c.6 0 1 .4 1 1 0 1.3.2 2.5.6 3.6.1.3 0 .7-.2 1z"/></svg>
    <div>: 1-855-555-0142</div>
  </div>
  <div class="contact-line abs" style="left:845px;top:256px">
    <svg width="20" height="16" viewBox="0 0 20 16" fill="none" stroke="#fff" stroke-width="1.5"><rect x="1" y="1" width="18" height="14"/><path d="M1 1l9 7 9-7"/></svg>
    <div>connect@brivelo.example</div>
  </div>
</footer>
<p class="copyright abs">© 2019 Company Name &nbsp;|&nbsp; All Rights Reserved</p>
<div class="social abs"><i></i><i></i><i></i></div>

</body>
</html>
```